Business Card Design - Law Firm

I need a business card design. I have attached a picture of the law firm's website and logo. The business card design should be consistent with those pictures. There should be a place for the employee name, employee job title, telephone number, facsimile number, address, website url, and email address for each employee.
Industry/Entity Type
Business

```html
<!DOCTYPE html>
<html lang="en">
<head>
<meta charset="utf-8">
<title>Aldermont Law – Business Card</title>
<link rel="stylesheet" href="https://fonts.googleapis.com/css2?family=Open+Sans:wght@400;600;700&family=Tinos:wght@400&display=swap">
<style>
  :root {
    --backdrop-center: #f7f6f7;
    --backdrop-edge: #b9b3b7;
    --card: #3b3b39;
    --card-light: #444442;
    --gold: #bb9a5c;
    --address-serif: #b9b7b3;
    --name-grey: #cfcfcf;
    --text-grey: #c4c4c2;
    --label-white: #f4f4f4;
    --rule: #bdbdbd;
    --mark: #1c1c1b;
  }
  html, body {
    margin: 0;
    padding: 0;
    width: 1200px;
    height: 916px;
    overflow: hidden;
  }
  .stage {
    position: relative;
    width: 1200px;
    height: 916px;
    background: radial-gradient(ellipse 70% 75% at 50% 52%, var(--backdrop-center) 0%, #e6e3e5 50%, var(--backdrop-edge) 100%);
  }
  .card {
    position: absolute;
    top: 334px;
    width: 402px;
    height: 246px;
    background: var(--card);
    border-radius: 24px 0 24px 0;
    overflow: hidden;
  }
  .card--front { left: 173px; }
  .card--back { left: 626px; }
  .card__texture {
    position: absolute;
    inset: 0;
    background: linear-gradient(115deg, var(--card) 0%, var(--card-light) 45%, var(--card) 100%);
  }
  /* front */
  .brand {
    position: absolute;
    left: 58px;
    top: 74px;
    display: flex;
    align-items: center;
    gap: 18px;
  }
  .brand__square {
    width: 48px;
    height: 48px;
    background: var(--mark);
  }
  .brand__name {
    font-family: "Tinos", "Times New Roman", serif;
    font-weight: 400;
    font-size: 35px;
    color: var(--gold);
    letter-spacing: 0.5px;
    white-space: nowrap;
  }
  .front-address {
    position: absolute;
    left: 0;
    width: 404px;
    top: 144px;
    padding-left: 0;
    text-align: center;
    font-family: "Tinos", "Times New Roman", serif;
    font-size: 13px;
    line-height: 15px;
    color: var(--address-serif);
    word-spacing: 3px;
  }
  /* back */
  .person {
    position: absolute;
    right: 23px;
    top: 68px;
    text-align: right;
    font-family: "Open Sans", Arial, sans-serif;
  }
  .person__name {
    font-size: 19px;
    font-weight: 700;
    color: var(--name-grey);
    letter-spacing: 0.3px;
    line-height: 26px;
  }
  .person__rule {
    width: 243px;
    height: 2px;
    background: var(--rule);
    margin: 1px 0 4px auto;
  }
  .person__title {
    font-size: 14px;
    color: var(--text-grey);
    line-height: 18px;
  }
  .contact {
    position: absolute;
    right: 23px;
    top: 131px;
    margin: 0;
    text-align: right;
    font-family: "Open Sans", Arial, sans-serif;
    font-size: 10.5px;
    color: var(--text-grey);
    line-height: 14px;
  }
  .contact p { margin: 0; }
  .contact .gap { margin-top: 2px; }
  .contact .gap-lg { margin-top: 3px; }
  .contact b { color: var(--label-white); font-weight: 700; }
</style>
</head>
<body>
<div class="stage">
  <section class="card card--front">
    <div class="card__texture" role="img" aria-label="Fine diagonal pinstripe texture on charcoal card"></div>
    <div class="brand">
      <div class="brand__square"></div>
      <div class="brand__name">Aldermont Law</div>
    </div>
    <div class="front-address">
      48 Wexley Road, Building 14<br>
      Halden, Maryland 2190
    </div>
  </section>

  <section class="card card--back">
    <div class="card__texture" role="img" aria-label="Fine diagonal pinstripe texture on charcoal card"></div>
    <div class="person">
      <div class="person__name">JONATHAN R</div>
      <div class="person__rule"></div>
      <div class="person__title">Executive Manager</div>
    </div>
    <div class="contact">
      <p><b>address</b> : 48 Wexley Road, Building 14</p>
      <p>Halden, Maryland 2190</p>
      <p><b>mobile</b> : 0412 7780 - <b>fax</b> : 2210 5536</p>
      <p class="gap"><b>email</b> : jonathan@aldermont.com</p>
      <p class="gap-lg"><b>web</b> : www.aldermontlaw.com</p>
    </div>
  </section>
</div>
</body>
</html>
```